Lantern's Hand: Project Rebuild & Restore

Design highly engaging brochure which will creatively communicate the vision, mission, history and core objectives of the new Lantern's Hand: Restore and Rebuild Project. (attached Below just updated today 8/27 at 1pm est)

- We will use this brochure to kick start our new 2014/2015 project "restore and rebuild" campaign
-Creative humanitarian inner curry look and feel

Dear Designers: Please DO NOT include "Ministry of Brookfield Fellowship Chapel" to any portion of the copy. Thanks, Owen

Creative must the following imagery: 1. have an urban look…revitalization of damaged homes being resurrected 2. Use core message on front and internal pages -"Rebuild and Restore" 3. use images that show volunteers restoring broken down homes: here is one example..please use your creative judgement to come up with new imagery: https://pics.quillorbit.example/view/rebuild-volunteers-01

Please see more examples of the creative approach we want to display in our brochure: https://pics.quillorbit.example/view/home-renewal-02

Dear Designers, We are updating the creative brief to include layout to include the following dimensions: 1.Pocket folder 9x12 with 3/8” white margin 2. 4 pg packet 11x17 folded to 8 ½ x11 Please design the brochure to the specs provided. Thanks!

Designers, WE HAVE INCREASED THE BUDGET. PLEASE SEE REVISED CREATIVE BRIEF!

Target Market(s)

Adults, US based, Norther New Jersey community, business men and women to support capital campaign

Industry/Entity Type

Campaign

Font styles to use
Serif

Requirements
Must have
• professional appeal, 3-4 page spread with clear communication of campaign objectives. Creative must align with the organization's vision and mission. Must include logo . Follow the colors within the attached logo. Also use the font from the website: http://lanternshandnj.example

Okay to use infographics and ICONs to clearly communicate the goal.

ADDITIONAL SPECS

1.Pocket folder 9x12 with 3/8” white margin
2. 4 pg packet 11x17 folded to 8 ½ x11

Nice to have
• Here's examples of work we like:

http://www.artvexo.example/design/1572779
http://www.artvexo.example/design/1777097
http://www.artvexo.example/design/4081213
http://www.artvexo.example/design/3992493
Should not have
• pic art, poor creative, no heart's. for this project we are leaving out Ministry of Brookfield Fellowship Chapel

```html
<!DOCTYPE html>
<html lang="en">
<head>
<meta charset="utf-8">
<title>Lantern's Hand – Rebuild and Restore Brochure Spread</title>
<link rel="stylesheet" href="https://fonts.googleapis.com/css2?family=Arimo:wght@400;700&family=Oswald:wght@500;600&display=swap">
<style>
  :root {
    --stage: #d4d4d6;
    --paper: #ffffff;
    --paper-shade: #ececec;
    --brand-red: #c3202e;
    --panel-red: rgba(190, 30, 45, 0.86);
    --ink: #3a3a3a;
    --ink-soft: #5a5a5a;
    --folio: #999999;
    --white: #ffffff;
  }
  * { box-sizing: border-box; margin: 0; padding: 0; }
  html, body {
    width: 1200px; height: 880px; overflow: hidden;
    background: var(--stage);
    font-family: "Arimo", Arial, sans-serif;
    color: var(--ink);
  }
  .spread {
    position: absolute; left: 50px; top: 60px;
    width: 1100px; height: 760px;
    display: flex;
    box-shadow: 0 10px 30px rgba(0,0,0,0.18);
  }
  .page {
    position: relative; width: 550px; height: 760px;
    background: var(--paper); overflow: hidden;
  }
  .page--left { background: linear-gradient(90deg, var(--paper) 88%, var(--paper-shade)); }
  .page--right { background: linear-gradient(90deg, var(--paper-shade), var(--paper) 12%); }

  .photo { position: absolute; }
  .photo--hands {
    left: 0; top: 0; width: 550px; height: 430px;
    background: linear-gradient(135deg, #2a2a2a 0%, #6f6f6f 35%, #b9b9b9 55%, #3c3c3c 100%);
  }
  .photo--builder {
    left: 0; top: 0; width: 550px; height: 300px;
    background: linear-gradient(120deg, #c9b48f 0%, #e9dcc3 40%, #b99a6c 70%, #8f98a6 100%);
  }

  .red-panel { position: absolute; background: var(--panel-red); color: var(--white); }
  .red-panel--history { left: 230px; top: 225px; width: 320px; height: 255px; padding: 16px 18px 12px 22px; }
  .red-panel--rebuild { left: 0; top: 165px; width: 345px; height: 315px; padding: 16px 20px 12px 20px; }

  .panel-title {
    font-family: "Oswald", "Arial Narrow", sans-serif; font-weight: 600;
    font-size: 14px; letter-spacing: 0.5px; text-transform: uppercase;
    margin-bottom: 4px;
  }
  .history-text { font-size: 7.6px; line-height: 1.32; }

  .q { font-weight: 700; font-size: 10.5px; margin: 6px 0 2px; }
  .q-list { list-style: none; font-size: 10px; line-height: 1.32; padding-left: 10px; }
  .q-list li::before { content: "• "; }

  .brand {
    position: absolute; left: 22px; top: 448px;
    display: flex; align-items: center; gap: 8px;
  }
  .brand__mark { width: 22px; height: 22px; background: var(--brand-red); }
  .brand__name {
    font-weight: 700; font-size: 15px; letter-spacing: 1px;
    color: var(--brand-red); text-transform: uppercase;
  }

  .label {
    position: absolute; background: var(--brand-red); color: var(--white);
    font-family: "Oswald", "Arial Narrow", sans-serif; font-weight: 500;
    font-size: 14px; letter-spacing: 0.6px; text-transform: uppercase;
    padding: 4px 14px;
  }
  .label--mission { left: 22px; top: 505px; }
  .label--background { left: 22px; top: 618px; }
  .label--values { left: 360px; top: 312px; width: 160px; }

  .body-copy { position: absolute; font-size: 11px; line-height: 1.35; color: var(--ink); }
  .mission-text { left: 22px; top: 542px; width: 500px; }

  .ring-list { list-style: none; font-size: 11px; line-height: 1.32; color: var(--ink); }
  .ring-list li { position: relative; padding-left: 16px; }
  .ring-list li::before {
    content: ""; position: absolute; left: 0; top: 3px;
    width: 7px; height: 7px; border: 1.3px solid var(--ink-soft); border-radius: 50%;
  }
  .background-list { position: absolute; left: 30px; top: 655px; width: 480px; }
  .values-list { position: absolute; left: 24px; top: 500px; width: 505px; font-size: 10.5px; }

  .folio { position: absolute; right: 18px; bottom: 14px; font-size: 9px; color: var(--folio); }
</style>
</head>
<body>
<main class="spread">
  <section class="page page--left">
    <div class="photo photo--hands" role="img" aria-label="Black and white photo of open hands holding a small cardboard house"></div>

    <div class="red-panel red-panel--history">
      <h2 class="panel-title">History</h2>
      <p class="history-text">The history of Lantern's Hand is found within the hearts of a few men from the North Jersey area with their gifts in construction and their hearts to help the poor. They decided to group together weekly and seek out opportunities to serve others with their hands and hearts. They decided Saturdays to volunteering as an act of worship to our Savior. This group started 30 years ago and has slowly turned into more than just a few men. We believe that His people would serve if someone could organize it and make it available to them. Within the last 5 years we have had well over 300 different volunteers with a larger degree of construction backgrounds and skills to help us construct houses, homeless shelters, relief organization's headquarters, gymnasiums, churches and rehabilitation centers. All these are among some of the projects that we have constructed. Within the last 3 years we have moved from working independently as a 501C3 to rather becoming part of the ministry of our local church. This move has been very exciting for all of our members and we feel right at home working thru the local church. The goal of Lantern's Hand is and will continue to be to bring joy to its workers hearts by being faithful to God's calling in their lives, to be a blessing in our community as a testimony to God, and to assist the Church in her ministry of service at large.</p>
    </div>

    <div class="brand">
      <span class="brand__mark"></span>
      <span class="brand__name">Lantern's Hand</span>
    </div>

    <h2 class="label label--mission">Mission Statement</h2>
    <p class="body-copy mission-text">Lantern's Hand is a group of organized individuals who serve the select needs of the church and various mission organizations. The purpose of this ministry is to perform service projects for both organizations and individuals, utilizing a trained team of volunteers (skilled and unskilled). Our efforts will reflect the love and power of Jesus Christ our Savior to build the Kingdom of God.</p>

    <h2 class="label label--background">Background</h2>
    <ul class="ring-list background-list">
      <li>Lantern's Hand is a 501(c)(3) tax-exempt organization - Donations and contributions are tax-deductible as allowed by law.</li>
      <li>Serving the community for over 30 years</li>
      <li>300+ volunteers</li>
      <li>Restoration projects including house constructions, homeless shelters, relief headquarters, gymnasiums, churches, and rehabilitation centers.</li>
    </ul>
  </section>

  <section class="page page--right">
    <div class="photo photo--builder" role="img" aria-label="Photo of a smiling volunteer in a yellow hard hat carrying timber inside a house under construction"></div>

    <div class="red-panel red-panel--rebuild">
      <h2 class="panel-title">Rebuild and Restore</h2>
      <p class="q">What's our goal?</p>
      <ul class="q-list">
        <li>The Lantern's Hand leadership has aligned with Beacon Point Ministries to identify community development opportunities with the purpose of creating long-term sustainable change in Paterson, New Jersey</li>
      </ul>
      <p class="q">How do we plan to reach our goal?</p>
      <ul class="q-list">
        <li>Rebuild - Leveraging our skills and gifts to remodel distressed homes with Paterson community</li>
        <li>Once restored, return the houses back to families within the Paterson community</li>
      </ul>
      <p class="q">What resources do we need?</p>
      <ul class="q-list">
        <li>We are seeking to procure 5 to 10 individual loans with the goal of raising $200,000 in start up capital costs.</li>
      </ul>
      <p class="q">What's our timeline?</p>
    </div>

    <h2 class="label label--values">Core Values</h2>
    <ul class="ring-list values-list">
      <li>To be in partnership with God where He is "the Head" and we are His hands, doing His work, showing His love to those whom He wills. Through our serving we can be a witness of our Lord Jesus and bring God all the glory.</li>
      <li>To meet the needs of select individuals, in the name of Jesus, to demonstrate His love for them.</li>
      <li>To assist mission organizations and churches to build and maintain the facilities they need for effective ministry.</li>
      <li>To be available for church authorities to do what God lays on their hearts needs to be done.</li>
      <li>To promote service and a servant's heart; the reasons for service, the attitude of service, the motive of service, and the rewards of service.</li>
      <li>To foster a community of fellowship, friendship, appreciation, love and caring among those who are involved in serving.</li>
      <li>To supply opportunities to be part of a ministry which has sought out opportunity, and broken it down into doable tasks so that many can utilize their gifts of service in a meaningful way.</li>
      <li>To train people in construction skills so they are able to help themselves and others both at home and through mission trips.</li>
    </ul>

    <span class="folio">15</span>
  </section>
</main>
</body>
</html>
```